Fun, easy to read post card design

Brindle Networks is looking for a designer to create a new (within theme) postcard design.

We have new internet packages rolling out and need to advertise it. Attached is a snippet from our website displaying those new internet plans, our logo and font.

https://www.brindlenetworks.ca/residential/

We would like the focus phrase to be "Fast, local reliable internet"

Let's see what you can come up with!

```html
<!DOCTYPE html>
<html lang="en">
<head>
<meta charset="utf-8">
<title>Brindle Networks Postcard</title>
<link rel="stylesheet" href="https://fonts.googleapis.com/css2?family=Montserrat:ital,wght@1,800;1,900&family=Open+Sans:wght@400;600;700&display=swap">
<style>
:root{
  --blue:#1ea4e0;
  --blue-deep:#1683c0;
  --ink:#2a2b2d;
  --slate:#3d3e41;
  --slate-dark:#262729;
  --paper:#f1f2f4;
  --white:#ffffff;
  --stage:#d6d7d9;
  --stamp:#c4c5c7;
  --rule:#b9babc;
}
*{margin:0;padding:0;box-sizing:border-box}
html,body{width:1200px;height:516px;overflow:hidden;background:var(--stage)}
body{position:relative;font-family:"Open Sans",Arial,sans-serif}
.card{position:absolute;top:74px;width:516px;height:368px;overflow:hidden;box-shadow:0 3px 10px rgba(0,0,0,.25)}
.card--front{left:74px;background:var(--paper)}
.card--back{left:610px;background:var(--white)}
.card-shapes{position:absolute;inset:0;width:516px;height:368px}
.abs{position:absolute}

/* front */
.brand{left:20px;top:16px;display:flex;align-items:center;gap:8px;color:var(--white);font-weight:700;font-size:17px}
.brand-dot{width:14px;height:14px;border-radius:50%;background:var(--white)}
.brand-caption{left:19px;top:99px;color:var(--blue);font-weight:600;font-size:17px}
.headline{right:10px;top:12px;width:140px;text-align:center;font-family:"Montserrat",Arial,sans-serif;font-style:italic;font-weight:900;font-size:15.5px;line-height:19.6px;text-transform:uppercase}
.headline .b{color:var(--blue)}
.headline .w{color:var(--white)}
.plans{left:22.5px;top:142px;display:flex;gap:6.5px}
.plan{width:89px;height:137px;background:linear-gradient(180deg,var(--slate-dark),var(--slate) 60%,#4a4b4e);color:var(--white);text-align:center}
.plan-name{height:29px;background:linear-gradient(180deg,var(--blue-deep),var(--blue));font-size:11.5px;font-weight:600;line-height:29px}
.plan-specs{margin:4px 3px 0;border-top:1px solid #8c8d90;border-bottom:1px solid #8c8d90;padding:6px 0 4px;font-size:6.4px;line-height:9.8px}
.plan-specs b{font-weight:700}
.plan-price{padding-top:6px;font-size:6.6px;line-height:7.8px}
.plan-price b{font-weight:700}
.cta{left:0;top:302px;width:516px;text-align:center;font-family:"Montserrat",Arial,sans-serif;font-style:italic;font-weight:900;font-size:25.5px;line-height:29.5px;color:var(--blue);text-transform:uppercase}

/* back */
.offer{left:28px;top:26px;font-family:"Montserrat",Arial,sans-serif;font-style:italic;font-weight:900;font-size:23.5px;line-height:30px;color:var(--blue);text-transform:uppercase}
.section-title{left:28px;color:var(--blue);font-weight:600;font-size:13.5px}
.why{top:94px}
.need{top:179px}
.lead{left:28px;top:123px;color:var(--white);font-size:7.5px;font-weight:600}
.reasons{left:28px;top:137px;width:360px;list-style:none;color:var(--white);font-size:7.5px;font-weight:600;line-height:9.8px}
.reasons li::before{content:"\2022";display:inline-block;width:11px}
.advice{left:28px;top:207px;width:282px;color:var(--white);font-size:7.6px;font-weight:600;line-height:9.8px}
.tollfree{left:28px;top:283px;font-family:"Montserrat",Arial,sans-serif;font-style:italic;font-weight:900;font-size:23.5px;line-height:29px;color:var(--blue)}
</style>
</head>
<body>

<section class="card card--front" aria-label="Postcard front">
  <svg class="card-shapes" viewBox="0 0 516 368" aria-hidden="true">
    <polygon points="0,0 250,0 204,102 0,102" fill="var(--blue-deep)"/>
    <polygon points="250,0 516,0 516,125 195,125 210,98" fill="var(--ink)"/>
    <rect x="0" y="294" width="516" height="74" fill="var(--slate)"/>
  </svg>
  <svg class="abs" style="left:0;top:0" width="516" height="125" viewBox="0 0 516 125" role="img" aria-label="Photo of a family cheering while watching a football match on television at home">
    <defs>
      <linearGradient id="photoTone" x1="0" y1="0" x2="1" y2="0">
        <stop offset="0" stop-color="#5a4a3e"/>
        <stop offset=".5" stop-color="#3a3230"/>
        <stop offset="1" stop-color="#1c1b1d"/>
      </linearGradient>
    </defs>
    <polygon points="262,0 516,0 516,125 206,125" fill="url(#photoTone)"/>
  </svg>

  <div class="abs brand"><span class="brand-dot"></span>Brindle Networks</div>
  <div class="abs brand-caption">Brindle Networks</div>

  <h1 class="abs headline">
    <span class="b">Keep</span><br><span class="w">Connected</span><br><span class="b">to what</span><br><span class="w">matters</span><br><span class="b">most</span>
  </h1>

  <div class="abs plans">
    <article class="plan"><div class="plan-name">SILVER</div>
      <div class="plan-specs">Download Speed<br><b>10 Mbps</b><br>Upload Speed<br><b>2 Mbps</b><br>Monthly Data<br><b>250GB</b></div>
      <div class="plan-price"><b>$69.95</b><br>per month</div></article>
    <article class="plan"><div class="plan-name">GOLD</div>
      <div class="plan-specs">Download Speed<br><b>20 Mbps</b><br>Upload Speed<br><b>3 Mbps</b><br>Monthly Data<br><b>500GB</b></div>
      <div class="plan-price"><b>$79.95</b><br>per month</div></article>
    <article class="plan"><div class="plan-name">PLATINUM</div>
      <div class="plan-specs">Download Speed<br><b>30 Mbps</b><br>Upload Speed<br><b>4 Mbps</b><br>Monthly Data<br><b>1000GB</b></div>
      <div class="plan-price"><b>$94.95</b><br>per month</div></article>
    <article class="plan"><div class="plan-name">ADVANCE</div>
      <div class="plan-specs">Download Speed<br><b>35 Mbps</b><br>Upload Speed<br><b>5 Mbps</b><br>Monthly Data<br><b>1200GB</b></div>
      <div class="plan-price"><b>$99.95</b><br>per month</div></article>
    <article class="plan"><div class="plan-name">UNLIMITED</div>
      <div class="plan-specs">Download Speed<br><b>35 Mbps</b><br>Upload Speed<br><b>5 Mbps</b><br>Monthly Data<br><b>UnlimitedGB</b></div>
      <div class="plan-price"><b>$149.95</b><br>per month</div></article>
  </div>

  <p class="abs cta">Sign up today<br>or call 1-780-555-0148</p>
</section>

<section class="card card--back" aria-label="Postcard back">
  <svg class="card-shapes" viewBox="0 0 516 368" aria-hidden="true">
    <polygon points="0,0 423,0 272,368 0,368" fill="var(--slate-dark)"/>
    <polygon points="423,0 429,0 278,368 272,368" fill="var(--blue)"/>
    <line x1="28" y1="90" x2="260" y2="90" stroke="var(--blue)" stroke-width="2.5"/>
    <circle cx="311" cy="73" r="44" fill="none" stroke="var(--blue)" stroke-width="6"/>
    <line x1="28" y1="279" x2="283" y2="279" stroke="var(--blue)" stroke-width="2.5"/>
    <rect x="419" y="28" width="74" height="74" fill="var(--stamp)"/>
    <line x1="330" y1="254" x2="493" y2="254" stroke="var(--rule)" stroke-width="1"/>
    <line x1="330" y1="289" x2="493" y2="289" stroke="var(--rule)" stroke-width="1"/>
    <line x1="330" y1="324" x2="493" y2="324" stroke="var(--rule)" stroke-width="1"/>
  </svg>

  <h2 class="abs offer">Free Install!<br>No Contracts!</h2>

  <h3 class="abs section-title why">Why Choose Brindle Networks?</h3>
  <p class="abs lead">What sets Brindle Networks apart:</p>
  <ul class="abs reasons">
    <li>Fast, local, reliable, internet access for your home</li>
    <li>You will get the speed you are paying for! No up to speeds, or prime time slowdowns!</li>
    <li>Great customer care for Alberta and Saskatchewan</li>
    <li>Multiple or customizable plan options to suit your needs and your budget</li>
  </ul>

  <h3 class="abs section-title need">What monthly traffic/speed do I need?</h3>
  <p class="abs advice">If you do only basic internet browsing and don’t spend much time on your computer, you should choose the silver plan. If you’re on your computer often and use email, social media, video streaming and downloading services, such as StreamBox and TuneShop, you should choose gold or platinum. If you have multiple internet users in your household who stream videos and play online video games, you should choose platinum or advanced.</p>

  <p class="abs tollfree">Toll Free:<br>1-866-555-0192</p>
</section>

</body>
</html>
```